Simplified Double Diamond Diagram for Book

I need a simplified version of the Double Diamond Diagram for a book I am working on. I would like to represent the diagram with the following image/text:
- Two diamonds connected (as in each of the sample photos)
- Inclusion of "Diverge" "Converge" above each of the sides of the diamonds as shown in sample image 1 - without elaborative text
- Inclusion of "Problem" and "Solution" in each diamond as is shown in the example image 2
- I need a color version and black/white version of the image that can be turned into a mono-color version in the book.

```html
<!DOCTYPE html>
<html lang="en">
<head>
<meta charset="utf-8">
<title>Double Diamond — Problem and Solution</title>
<link href="https://fonts.googleapis.com/css2?family=Lato:wght@700;900&display=swap" rel="stylesheet">
<style>
  :root {
    --page: #ffffff;
    --problem-light: #245b73;
    --problem-dark: #143f5e;
    --problem-edge: #1b2a4a;
    --problem-label: #1f4e68;
    --solution-light: #f7901e;
    --solution-dark: #f57a15;
    --solution-edge: #f45a10;
    --solution-label: #f7901e;
    --centre-text: #ffffff;
  }
  html, body {
    margin: 0;
    padding: 0;
    width: 1200px;
    height: 796px;
    overflow: hidden;
    background: var(--page);
  }
  .diagram {
    display: block;
    width: 1200px;
    height: 796px;
  }
  .edge-label {
    font-family: "Lato", sans-serif;
    font-weight: 900;
    font-size: 17px;
    letter-spacing: 0.3px;
    text-anchor: middle;
    dominant-baseline: middle;
  }
  .problem .edge-label { fill: var(--problem-label); }
  .solution .edge-label { fill: var(--solution-label); }
  .centre-label {
    font-family: "Lato", sans-serif;
    font-weight: 700;
    font-size: 21px;
    fill: var(--centre-text);
    text-anchor: middle;
    dominant-baseline: middle;
  }
  .problem .half-left { fill: var(--problem-light); }
  .problem .half-right { fill: var(--problem-dark); }
  .problem .outline, .problem .tick { stroke: var(--problem-edge); }
  .solution .half-left { fill: var(--solution-light); }
  .solution .half-right { fill: var(--solution-dark); }
  .solution .outline, .solution .tick { stroke: var(--solution-edge); }
  .outline { fill: none; stroke-width: 5; stroke-linejoin: miter; }
  .tick { stroke-width: 5; }
</style>
</head>
<body>
<svg class="diagram" viewBox="0 0 860 570" xmlns="http://www.w3.org/2000/svg" role="img" aria-label="Double diamond diagram: problem diamond and solution diamond, each with divergent discover and convergent define phases">
  <g class="problem">
    <line class="tick" x1="91" y1="277" x2="109" y2="313"/>
    <polygon class="half-left" points="110,294 270,132 270,458"/>
    <polygon class="half-right" points="270,132 432,294 270,458"/>
    <polygon class="outline" points="110,294 270,132 432,294 270,458"/>
    <text class="centre-label" x="271" y="294">PROBLEM</text>
    <text class="edge-label" transform="translate(181,195) rotate(-45)">DIVERGENT</text>
    <text class="edge-label" transform="translate(364,195) rotate(45)">CONVERGENT</text>
    <text class="edge-label" transform="translate(170,393) rotate(45)">DISCOVER</text>
    <text class="edge-label" transform="translate(368,393) rotate(-45)">DEFINE</text>
  </g>
  <g class="solution">
    <line class="tick" x1="757" y1="277" x2="775" y2="313"/>
    <polygon class="half-left" points="432,294 595,132 595,458"/>
    <polygon class="half-right" points="595,132 755,294 595,458"/>
    <polygon class="outline" points="432,294 595,132 755,294 595,458"/>
    <text class="centre-label" x="595" y="294">SOLUTION</text>
    <text class="edge-label" transform="translate(505,195) rotate(-45)">DIVERGENT</text>
    <text class="edge-label" transform="translate(688,195) rotate(45)">CONVERGENT</text>
    <text class="edge-label" transform="translate(494,393) rotate(45)">DISCOVER</text>
    <text class="edge-label" transform="translate(692,393) rotate(-45)">DEFINE</text>
  </g>
</svg>
</body>
</html>
```